We require a fully editable Olive Oil Label.
We need a front label with the following on it:
- Name (Tovaro's Wren)
- Graphic (Gold olives on branch dripping oil, clear background)
- 100% Extra Virgin Olive Oil
- Size (3L)
We need a back label with the following on it:
- Blurb: We are a 100% Australian owned family olive grove & olive oil production company. We are dedicated to producing the highest quality product possible. Proudly grown, processed & packaged in Millbrook NSW.
- Nutritional information table
- Ingredients
- Organic certification logo (in gold, clear background)
- Contact details
- Batch number placeholder
- Expiry date placeholder
- Barcode
- Store in a cool dry place. Do not refrigerate.
It will be for a rectangular bottle.
Our vision is that the background would be matt black, writing could be gold, white or red, 'Tovaro's' would be red & above a gold olives on branch dripping oil, while 'Mrs' would be red & below the gold olive branch. Tovaro's Wren would be in similar font to the Tovaro image attached. We are thinking maybe a Pop Art or Modern feel to the label but are happy to look at anything you think may be appropriate or look better then our thoughts. We are open to suggestions. We have included examples of other labels for layout reference.
Thanks!

```html
<!DOCTYPE html>
<html lang="en">
<head>
<meta charset="utf-8">
<title>Tovaro's Wren – Olive Oil Labels</title>
<link rel="stylesheet" href="https://fonts.googleapis.com/css2?family=Roboto+Condensed:wght@400;700&family=Roboto:wght@400;700&family=Great+Vibes&display=swap">
<style>
  :root {
    --canvas: #f4f4f4;
    --label-black: #1c1a1a;
    --brand-red: #e8323a;
    --gold: #e2b736;
    --gold-deep: #b8902a;
    --white: #ffffff;
    --ink: #231f20;
    --olive-light: #d9c25a;
    --olive-dark: #7a6a22;
  }
  * { box-sizing: border-box; margin: 0; padding: 0; }
  html, body {
    width: 1200px; height: 1200px; overflow: hidden;
    background: var(--canvas);
    font-family: "Roboto", Arial, sans-serif;
  }
  .canvas { position: relative; width: 1200px; height: 1200px; }

  .label {
    position: absolute; top: 170px;
    width: 300px; height: 860px;
    overflow: hidden;
    background: var(--label-black);
    box-shadow: 0 6px 18px rgba(0,0,0,.18);
  }
  .label--back { left: 75px; }
  .label--front-red { left: 450px; }
  .label--front-white { left: 825px; }

  .label__shape { position: absolute; inset: 0; width: 300px; height: 860px; }

  /* Back label */
  .blurb {
    position: absolute; top: 150px; left: 26px; width: 248px;
    text-align: center;
    font: 700 16px/1.24 "Roboto", Arial, sans-serif;
    color: var(--ink);
  }
  .ingredients {
    position: absolute; top: 412px; left: 14px; width: 272px;
    font: 400 10.5px/1.35 "Roboto", Arial, sans-serif;
    color: var(--white);
  }
  .ingredients__title {
    font: 400 15px "Roboto Condensed", Arial, sans-serif;
    color: var(--gold);
  }
  .facts {
    position: absolute; top: 462px; left: 14px; width: 272px;
    background: var(--white);
    border: 3px solid var(--gold);
    padding: 4px 6px 6px;
    color: var(--ink);
    font: 400 8.5px/1.25 "Roboto", Arial, sans-serif;
  }
  .facts__title {
    font: 700 17px "Roboto Condensed", Arial, sans-serif;
    border-bottom: 3px solid var(--ink);
    padding-bottom: 2px; margin-bottom: 2px;
  }
  .facts__row {
    display: flex; justify-content: space-between;
    border-bottom: 1px solid #bbb; padding: 2px 0;
  }
  .facts__row--bold { font-weight: 700; border-bottom: 2px solid var(--ink); }
  .facts__note { margin-top: 6px; font-size: 8px; }

  .storage-note {
    position: absolute; left: 16px; top: 830px;
    transform: rotate(-90deg); transform-origin: 0 0;
    width: 130px;
    font: 400 8px/1.25 "Roboto", Arial, sans-serif;
    color: var(--gold);
  }
  .maker-details {
    position: absolute; top: 690px; left: 118px; width: 170px;
    font: 700 8.5px/1.3 "Roboto", Arial, sans-serif;
    color: var(--white);
  }
  .maker-details p + p { margin-top: 6px; }

  /* Front labels */
  .brand {
    position: absolute; top: 62px; left: 0; width: 300px;
    display: flex; align-items: center; justify-content: center; gap: 8px;
    font: 400 20px "Roboto", Arial, sans-serif;
    color: var(--ink);
  }
  .brand__dot { width: 14px; height: 14px; border-radius: 50%; background: var(--gold-deep); }
  .product-type {
    position: absolute; top: 112px; left: 0; width: 300px; text-align: center;
    font: 400 27px "Roboto Condensed", Arial, sans-serif;
  }
  .product-name {
    position: absolute; top: 138px; left: 0; width: 300px; text-align: center;
    font: 400 64px/1 "Roboto", Arial, sans-serif;
  }
  .grade {
    position: absolute; top: 212px; left: 0; width: 300px; text-align: center;
    font: 400 20px "Great Vibes", cursive;
  }
  .label--front-red .product-type,
  .label--front-red .product-name { color: var(--white); }
  .label--front-red .grade { color: var(--ink); }
  .label--front-white .product-type,
  .label--front-white .product-name,
  .label--front-white .grade { color: var(--ink); }

  .olive-art {
    position: absolute; top: 390px; left: 70px; width: 190px; height: 230px;
    border-radius: 40% 60% 45% 55%;
    background: radial-gradient(ellipse at 45% 45%, var(--olive-light) 0%, var(--olive-dark) 55%, rgba(28,26,26,0) 75%);
    opacity: .85;
  }
  .leaf-texture {
    position: absolute; top: 620px; left: 30px; width: 240px; height: 200px;
    background: radial-gradient(ellipse at 50% 50%, rgba(255,255,255,.06), rgba(255,255,255,0) 70%);
  }
  .cert-badge {
    position: absolute; top: 748px; left: 18px;
    width: 64px; height: 64px; border-radius: 50%;
    background: var(--gold);
    border: 3px solid var(--gold-deep);
  }
  .net-weight {
    position: absolute; top: 768px; right: 22px;
    font: 700 19px "Roboto", Arial, sans-serif;
    color: var(--gold);
  }
</style>
</head>
<body>
<main class="canvas">

  <!-- Back label -->
  <section class="label label--back">
    <svg class="label__shape" viewBox="0 0 300 860" aria-hidden="true">
      <path d="M0 0H300V330C220 385 90 395 0 345Z" fill="var(--brand-red)"/>
      <path d="M0 345C90 395 220 385 300 330V350C220 410 90 415 0 368Z" fill="var(--gold)"/>
      <path d="M0 372C90 418 220 414 300 356V364C220 424 90 428 0 382Z" fill="var(--brand-red)"/>
    </svg>
    <p class="blurb">We are a 100% Australian owned family olive grove &amp; olive oil production company. We are dedicated to producing the highest quality product possible. Proudly grown, processed &amp; packaged in Millbrook NSW.</p>
    <p class="ingredients"><span class="ingredients__title">Ingredients:</span> Lorem Ipsum is simply dummy text of the printing and typesetting industry. Lorem Ipsum has been the industry's</p>
    <div class="facts">
      <div class="facts__title">SUPPLEMENT FACTS</div>
      <div class="facts__row"><span>Serving Size:</span><span>1 Dropper (1ml)</span></div>
      <div class="facts__row facts__row--bold"><span>Serving Per Container:</span><span>30</span></div>
      <div class="facts__row"><span>Amount per Serving</span><span>%DV</span></div>
      <div class="facts__row"><span>Calories:</span><span>10</span></div>
      <div class="facts__row"><span>Total fat</span><span>1g &nbsp;&nbsp;&nbsp; 2%</span></div>
      <div class="facts__row"><span>Hemp Extract &nbsp;&nbsp; 16.67mg</span><span>†</span></div>
      <div class="facts__row"><span>(Leaves &amp; Flowers)</span><span></span></div>
      <div class="facts__row facts__row--bold"><span>[15mg cannabidiol (CBD)]</span><span></span></div>
      <p class="facts__note">* Percent Daily Values (DV) are based on a 2,000 Calorie diet † Daily Value not established.</p>
    </div>
    <p class="storage-note">Store in a cool dry place.<br>Do not refrigerate.</p>
    <div class="maker-details">
      <p>Batch #<br>Manufactured Date:<br>Manufactured in Australia For<br>TOVARO 0400 000 000</p>
      <p>Manufactured By<br>TOVARO<br>12 Orchard Lane, Suite 4<br>Millbrook NSW 2700</p>
    </div>
  </section>

  <!-- Front label, red -->
  <section class="label label--front-red">
    <svg class="label__shape" viewBox="0 0 300 860" aria-hidden="true">
      <path d="M0 0H300V250C220 300 90 310 0 262Z" fill="var(--brand-red)"/>
      <path d="M0 262C90 310 220 300 300 250V270C220 325 90 330 0 284Z" fill="var(--gold)"/>
      <path d="M0 288C90 334 220 330 300 276V284C220 342 90 346 0 298Z" fill="var(--brand-red)"/>
    </svg>
    <div class="brand"><span class="brand__dot"></span>Grove House Oils</div>
    <p class="product-type">100% Extra Virgin</p>
    <p class="product-name">Olive Oil</p>
    <p class="grade">Premium Quality</p>
    <div class="olive-art" role="img" aria-label="Gold olives on a branch dripping oil"></div>
    <div class="leaf-texture" role="img" aria-label="Faint olive leaf pattern"></div>
    <div class="cert-badge" aria-label="Organic certification badge"></div>
    <p class="net-weight">NET WT:3L</p>
  </section>

  <!-- Front label, white -->
  <section class="label label--front-white">
    <svg class="label__shape" viewBox="0 0 300 860" aria-hidden="true">
      <path d="M0 0H300V250C220 300 90 310 0 262Z" fill="var(--white)"/>
      <path d="M0 262C90 310 220 300 300 250V270C220 325 90 330 0 284Z" fill="var(--gold)"/>
      <path d="M0 288C90 334 220 330 300 276V284C220 342 90 346 0 298Z" fill="var(--white)"/>
    </svg>
    <div class="brand"><span class="brand__dot"></span>Grove House Oils</div>
    <p class="product-type">100% Extra Virgin</p>
    <p class="product-name">Olive Oil</p>
    <p class="grade">Premium Quality</p>
    <div class="olive-art" role="img" aria-label="Gold olives on a branch dripping oil"></div>
    <div class="leaf-texture" role="img" aria-label="Faint olive leaf pattern"></div>
    <div class="cert-badge" aria-label="Organic certification badge"></div>
    <p class="net-weight">NET WT:3L</p>
  </section>

</main>
</body>
</html>
```